Industrial Professional Business Card Design (Vantrel Systems)

Would like professional looking business cards. Not too busy leaning towards minimal. Should have a slogan like:
"Industrial Automation and Control".

We are a tech company that programs industrial PLC computers. We also develop custom hardware solutions. Please use the logo for inspiration.

Target Market(s)

Mining, industrial, processing, automation, factory

Industry/Entity Type

Engineering

Contact Information for Business Card

Name, phone, email, website. job title.

Font styles to use
Other font styles liked:
• droid sans

Requirements
Must have
• Use colours that go well with the logo. Not too busy design.

```html
<!DOCTYPE html>
<html lang="en">
<head>
<meta charset="utf-8">
<title>Vantrel Systems — Business Card</title>
<link rel="stylesheet" href="https://fonts.googleapis.com/css2?family=Noto+Sans:wght@400;700&display=swap">
<style>
  :root {
    --navy: #1d4c74;
    --name-blue: #1f5a8c;
    --orange: #f26522;
    --ink: #111111;
    --paper: #ffffff;
    --edge: #9a9a9a;
  }
  * { box-sizing: border-box; margin: 0; padding: 0; }
  html, body { width: 1200px; height: 1200px; overflow: hidden; background: var(--paper); }
  body { position: relative; font-family: "Noto Sans", sans-serif; color: var(--ink); }

  .card {
    position: absolute;
    left: 288px;
    width: 736px;
    height: 450px;
    background: var(--paper);
    border: 1px solid var(--edge);
    overflow: hidden;
  }
  .card--front { top: 98px; }
  .card--back { top: 621px; }

  .card__bands { position: absolute; inset: 0; width: 100%; height: 100%; }
  .band-navy { fill: var(--navy); }
  .band-orange { fill: var(--orange); }

  .card__web {
    position: absolute; left: 81px; top: 3px;
    font-size: 23px; color: var(--paper); letter-spacing: 0.2px;
  }
  .card__footer-text {
    position: absolute; left: 126px; right: 0; top: 412px; height: 38px;
    display: flex; align-items: center; justify-content: center;
    font-size: 22px; color: var(--paper);
  }

  .brand {
    position: absolute;
    display: flex; flex-direction: column; align-items: center;
    transform: translate(-50%, -50%);
  }
  .brand__dot { border-radius: 50%; background: var(--orange); }
  .brand__name { color: var(--navy); font-weight: 400; white-space: nowrap; }

  .brand--front { left: 236px; top: 212px; }
  .brand--front .brand__dot { width: 62px; height: 62px; margin-bottom: 14px; }
  .brand--front .brand__name { font-size: 30px; }

  .brand--back { left: 368px; top: 216px; }
  .brand--back .brand__dot { width: 112px; height: 112px; margin-bottom: 24px; }
  .brand--back .brand__name { font-size: 48px; }

  .divider {
    position: absolute; left: 366px; top: 157px;
    width: 4px; height: 134px; background: var(--name-blue);
  }

  .contact { position: absolute; left: 393px; top: 150px; }
  .contact__name { font-size: 25px; font-weight: 700; color: var(--name-blue); line-height: 1.2; letter-spacing: 0.3px; }
  .contact__role { font-size: 22px; line-height: 1.2; margin-left: 2px; }
  .contact__list { list-style: none; margin-top: 16px; }
  .contact__item { display: flex; align-items: center; gap: 12px; font-size: 22px; line-height: 32px; }
  .contact__icon { width: 24px; height: 24px; flex: none; }
  .icon-disc { fill: var(--name-blue); }
  .icon-line { fill: none; stroke: var(--paper); stroke-width: 1.6; stroke-linejoin: round; }
</style>
</head>
<body>

<section class="card card--front" aria-label="Business card front">
  <svg class="card__bands" viewBox="0 0 736 450" aria-hidden="true">
    <polygon class="band-navy" points="0,0 399,0 375,38 0,38"/>
    <polygon class="band-orange" points="138,405 736,405 736,410 135,410"/>
    <polygon class="band-navy" points="0,441 107,441 126,410 736,410 736,450 0,450"/>
  </svg>
  <p class="card__web">www.vantrelsystems.com</p>

  <div class="brand brand--front">
    <span class="brand__dot" aria-hidden="true"></span>
    <span class="brand__name">Vantrel Systems</span>
  </div>

  <span class="divider" aria-hidden="true"></span>

  <div class="contact">
    <h1 class="contact__name">PERSON NAME</h1>
    <p class="contact__role">Manager</p>
    <ul class="contact__list">
      <li class="contact__item">
        <svg class="contact__icon" viewBox="0 0 24 24" aria-hidden="true">
          <circle class="icon-disc" cx="12" cy="12" r="12"/>
          <path fill="#fff" d="M8.2 6.2l2 2.3-1.1 1.6c.8 1.8 2.1 3.1 3.9 3.9l1.6-1.1 2.3 2-1.3 2c-4.6-.6-8.4-4.4-9-9z"/>
        </svg>
        <span>+91 9800012345</span>
      </li>
      <li class="contact__item">
        <svg class="contact__icon" viewBox="0 0 24 24" aria-hidden="true">
          <circle class="icon-disc" cx="12" cy="12" r="12"/>
          <rect class="icon-line" x="5.5" y="8" width="13" height="8.5"/>
          <path class="icon-line" d="M5.5 8l6.5 5 6.5-5M5.5 16.5l4.8-4.3M18.5 16.5l-4.8-4.3"/>
        </svg>
        <span>info@vantrelsystems.com</span>
      </li>
    </ul>
  </div>

  <p class="card__footer-text">18, Kesar Villa, Harbour Road, Bandra</p>
</section>

<section class="card card--back" aria-label="Business card back">
  <svg class="card__bands" viewBox="0 0 736 450" aria-hidden="true">
    <polygon class="band-navy" points="0,0 399,0 375,38 0,38"/>
    <polygon class="band-orange" points="138,405 736,405 736,410 135,410"/>
    <polygon class="band-navy" points="0,441 107,441 126,410 736,410 736,450 0,450"/>
  </svg>

  <div class="brand brand--back">
    <span class="brand__dot" aria-hidden="true"></span>
    <span class="brand__name">Vantrel Systems</span>
  </div>

  <p class="card__footer-text">Industrial Automation and Control</p>
</section>

</body>
</html>
```